Wordpress Web Design & Coding for velqorahealth.ca

We need a website for a new investment company that is visually grabbing and vibrant. We would like to see a web page that displays trust, growth and confidence. Needs to be responsive and mobile friendly for all browsers and coded for both Android & IOS.

Open to the number of pages and menu items. I selected 4 but if you feel the layout would work better with less I am open to this. Need to sell the people (management team/related businesses) and then show where the invested money will be going (upcoming projects).

Company Info:

Velq Ora is an investment company put together by a group of seasoned business professionals who have come together to combine decades of success in the real estate development, management, financing and medical services. The company will be a full service company offering turn key solutions for medical professionals.

Velq-Ora will focus on providing a full range of services via a group of distinct companies to deliver newly emerging needs of the medical community. The end goal will be to create complete solutions for individuals in the medical community. Our group has experience and success with the conceptualization, construction and financing of medical and dental clinic spaces. Velq-Ora Solutions will be established to accommodate all areas of the development and creation of clinics for medical professionals from building construction to equipment financing and administrations.

You can mention these companies and take photos from their websites. You can also use stock photos.

Our construction partner:
https://812bld.com/projects/

Our equipment leasing partner:
https://www.lomerix.com/

Our Management Team and medical partners

Dale Pickett
https://www.yourcalmpath.ca/

Milos Vandergrift
https://www.qhzdentalservices.com/about-us

PROPOSED PROJECTS (see attachment for details)
Harlow Ridge Business Park
Dunmere Business Park
Mt. Corwin Way Professional

Target Market(s)

Investors

Industry/Entity Type

Investment

Coding

Coded - Design and coding required

Number of Pages Required

4 page

Font styles to use
Sans Serif

Requirements
Must have
• Wordpress – must be both desktop and mobile friendly with fast page load speed
Ability to edit after ourselves in Wordpress
Attractive home page with logo etc.
Logo colours are: for the blue the pantone color is #0355a3
and for the green is #8cc63f

Sections, about us, what we do/services we provide, contact us

```html
<!DOCTYPE html>
<html lang="en">
<head>
<meta charset="utf-8">
<title>Velq-Ora Solutions</title>
<link href="https://fonts.googleapis.com/css2?family=Roboto:wght@300;400;500;700&family=Noto+Serif:wght@400&display=swap" rel="stylesheet">
<style>
:root{
  --blue:#0355a3;
  --blue-mid:#2a68b3;
  --blue-soft:#3a73b8;
  --green:#8cc63f;
  --grey-bg:#f3f3f3;
  --text:#555;
  --text-light:#8a8a8a;
  --dark:#333;
  --darker:#262626;
  --white:#fff;
}
*{box-sizing:border-box;margin:0;padding:0}
html,body{width:1200px;height:3304px;overflow:hidden}
body{position:relative;font-family:'Roboto',Arial,sans-serif;color:var(--text);background:var(--white)}
.abs{position:absolute}
.btn{position:absolute;display:flex;align-items:center;justify-content:center;background:var(--green);color:var(--white);font-weight:500;font-size:15px;border-radius:3px}
.stripes{position:absolute;height:8px;background:repeating-linear-gradient(115deg,var(--green) 0 2px,transparent 2px 5px)}
.stripes.light{background:repeating-linear-gradient(115deg,rgba(255,255,255,.55) 0 2px,transparent 2px 5px)}
.section-title{position:absolute;font-weight:300;font-size:31px;letter-spacing:.5px}

/* header */
.site-header{position:absolute;left:0;top:0;width:1200px;height:88px;background:var(--white)}
.brand{position:absolute;left:78px;top:22px;width:150px;font-weight:700;font-size:17px;line-height:20px;color:var(--blue);letter-spacing:.5px;display:flex;align-items:center;gap:8px}
.brand-dot{flex:none;width:12px;height:12px;background:var(--green)}
.main-nav a{position:absolute;top:24px;height:40px;line-height:40px;font-size:12px;font-weight:500;color:#555;text-decoration:none}
.main-nav a.current{border:2px solid var(--green);color:var(--green);padding:0 14px;line-height:36px}
.call-icon{position:absolute;left:900px;top:20px;width:42px;height:42px;border-radius:50%;background:var(--blue)}
.call-number{position:absolute;left:950px;top:20px;font-size:22px;font-weight:700;color:var(--green)}
.call-note{position:absolute;left:951px;top:48px;font-size:13px;color:#666}

/* hero */
.hero-photo{position:absolute;left:0;top:88px;width:600px;height:504px;background:linear-gradient(160deg,#4a80c0 0%,#2a62a8 45%,#1d4f93 100%)}
.hero-panel{position:absolute;left:600px;top:88px;width:600px;height:512px;background:var(--grey-bg)}
.hero-title{position:absolute;left:645px;top:156px;font-weight:300;font-size:45px;line-height:54px;color:var(--blue)}
.hero-title span{color:var(--green);display:block}
.hero-text{position:absolute;left:645px;top:316px;width:515px;font-size:13.5px;line-height:24px;color:#555}

/* about */
.about-text{position:absolute;left:138px;top:728px;width:440px;font-size:13px;line-height:24px;color:#555}
.brand-mark-area{position:absolute;left:720px;top:718px;width:268px;height:252px;background:radial-gradient(circle at 50% 50%,#e8f0f9 0%,#f7fafc 70%,#fff 100%);border-radius:4px}

/* what we do */
.band{position:absolute;left:0;width:1200px;overflow:hidden}
.band-bg{position:absolute;inset:0;background:linear-gradient(135deg,#1f5aa5 0%,#0f4c98 40%,#2a68b0 70%,#1a57a2 100%)}
.band svg{position:absolute;left:0;width:1200px}
.service-card{position:absolute;top:1306px;width:313px;height:275px;background:var(--white);text-align:center}
.service-card svg{position:absolute;left:118px;top:26px}
.service-card h3{position:absolute;left:0;top:112px;width:100%;font-size:19px;line-height:26px;font-weight:500;color:var(--blue)}
.service-card p{position:absolute;left:22px;top:176px;width:269px;font-size:13.5px;line-height:24px;color:#666}

/* projects */
.project-photo{position:absolute;left:102px;top:1890px;width:498px;height:400px;background:linear-gradient(180deg,#5d8fc4 0%,#a9c4df 45%,#d9d9d4 62%,#5b5650 80%,#3e3a36 100%)}
.project-name{position:absolute;left:655px;top:1930px;font-size:25px;font-weight:300;color:#555}
.project-sub{position:absolute;left:655px;top:1968px;font-size:14px;color:var(--text-light)}
.project-text{position:absolute;left:655px;top:2016px;width:430px;font-family:'Noto Serif',Georgia,serif;font-size:14px;line-height:21px;color:#666}
.slide-btn{position:absolute;width:53px;height:53px;background:var(--blue-soft);display:flex;align-items:center;justify-content:center}

/* callback */
.callback-form{position:absolute;left:289px;top:2538px;width:623px;height:400px;background:rgba(255,255,255,.96);border-radius:6px}
.field{position:absolute;left:44px;width:534px;height:41px;border:1px solid #ccc;background:var(--white);font-size:13px;color:#666;padding:12px 14px}
.send{position:absolute;left:44px;top:313px;width:534px;height:41px;background:var(--green);color:var(--white);font-size:14px;font-weight:500;display:flex;align-items:center;justify-content:center}

/* footer */
.site-footer{position:absolute;left:0;top:2990px;width:1200px;height:238px;background:var(--dark)}
.footer-brand{position:absolute;left:155px;top:3090px;font-size:22px;font-weight:700;color:var(--blue-soft);display:flex;align-items:center;gap:8px}
.social{position:absolute;top:3143px;width:28px;height:28px;border-radius:3px}
.footer-col h4{position:absolute;top:3043px;font-size:20px;font-weight:300;color:var(--white);letter-spacing:.5px}
.footer-col a,.footer-col span{position:absolute;font-size:13px;color:#eee;text-decoration:none;line-height:22px}
.copyright{position:absolute;left:0;top:3228px;width:1200px;height:76px;background:var(--darker);color:var(--white);font-size:13px;display:flex;align-items:center;justify-content:center}
</style>
</head>
<body>

<header class="site-header">
  <div class="brand"><span class="brand-dot"></span><span>VELQ-ORA<br>SOLUTIONS</span></div>
  <nav class="main-nav">
    <a class="current" style="left:300px">Home</a>
    <a style="left:391px">About Us</a>
    <a style="left:483px">What We Do</a>
    <a style="left:591px">Our Projects</a>
    <a style="left:702px">Contact Us</a>
  </nav>
  <div class="call-icon">
    <svg width="42" height="42" viewBox="0 0 42 42"><path d="M15 12c1-1 2-1 3 0l2 3c.6 1 .3 2-.5 2.6l-1.3 1c.8 2 2.3 3.6 4.2 4.4l1-1.3c.6-.8 1.7-1 2.6-.5l3 2c1 .7 1 2 0 3l-1.5 1.5c-1.3 1.3-3.5 1.5-6-0.2-3.5-2.3-6.5-5.5-8.5-9-1.5-2.6-1.2-4.6.2-5.8z" fill="#fff"/></svg>
  </div>
  <div class="call-number">812-406-7719</div>
  <div class="call-note">Call us now for more info</div>
</header>

<section>
  <div class="hero-photo" role="img" aria-label="Blue-tinted photo of a two-storey commercial building"></div>
  <div class="hero-panel"></div>
  <h1 class="hero-title">Invest in<span>Your Trusted Company</span></h1>
  <p class="hero-text">Velq Ora is an investment company put together by a group of seasoned business professionals who have come together to combine decades of success in the real estate development, management, financing and medical services. The company will be a full service company offering turn key solutions for medical professionals.</p>
  <div class="btn" style="left:645px;top:470px;width:140px;height:52px">More Info</div>
</section>

<section>
  <h2 class="section-title" style="left:138px;top:645px;color:var(--blue)">ABOUT US</h2>
  <div class="stripes" style="left:138px;top:698px;width:152px"></div>
  <p class="about-text">Velq-Ora will focus on providing a full range of services via a group of distinct companies to deliver newly emerging needs of the medical community. The end goal will be to create complete solutions for individuals in the medical community. Our group has experience and success with the conceptualization, construction and financing of medical and dental clinic spaces. Velq-Ora Solutions will be established to accommodate all areas of the development and creation of clinics for medical professionals from building construction to equipment financing and administrations.</p>
  <div class="btn" style="left:138px;top:977px;width:320px;height:52px">Our Management Team &amp; Partners</div>
  <div class="brand-mark-area" role="img" aria-label="Large company brand mark"></div>
</section>

<section class="band" style="top:1085px;height:643px">
  <div class="band-bg" role="img" aria-label="Blue-tinted photo of a glass office building"></div>
  <svg height="643" viewBox="0 0 1200 643">
    <polygon points="0,0 1200,0 1200,55 600,10 0,40" fill="#fff" opacity=".85"/>
    <polygon points="0,0 500,0 0,30" fill="#fff" opacity=".4"/>
    <polygon points="0,643 1200,643 1200,600 600,635 0,595" fill="#fff" opacity=".85"/>
    <polygon points="0,643 0,575 700,643" fill="#fff" opacity=".3"/>
  </svg>
</section>
<h2 class="section-title" style="left:0;width:1200px;text-align:center;top:1132px;color:var(--white)">WHAT WE DO</h2>
<div class="stripes light" style="left:425px;top:1187px;width:350px"></div>
<p class="abs" style="left:0;top:1213px;width:1200px;text-align:center;color:var(--white);font-size:22px;line-height:33px;font-weight:300">Velq-Ora Solutions established to accommodate all areas of the development and creation of<br><span style="font-weight:400">clinics for medical professionals</span></p>

<div class="service-card" style="left:112px">
  <svg width="76" height="76" viewBox="0 0 76 76" fill="none" stroke="#8cc63f" stroke-width="2"><path d="M20 74V8h8v66M20 14H72M28 8l44 6M14 14h6M46 14v22M38 46h16v14H38zM40 46l6-10 6 10M6 74h66"/></svg>
  <h3>Medical Building<br>Construction</h3>
  <p>Lorem ipsum dolor sit amet, consectetur adipiscing elit. Ut elit tellus, luctus nec ullamcorper mattis, pulvinar dapibus leo.</p>
</div>
<div class="service-card" style="left:443px">
  <svg width="76" height="76" viewBox="0 0 76 76" fill="none" stroke="#8cc63f" stroke-width="2"><path d="M4 28h46v24H4zM8 20l40-8 4 16"/><circle cx="27" cy="40" r="7"/><ellipse cx="62" cy="44" rx="9" ry="4"/><path d="M53 44v22c0 2 4 4 9 4s9-2 9-4V44M53 51c0 2 4 4 9 4s9-2 9-4M53 58c0 2 4 4 9 4s9-2 9-4"/></svg>
  <h3>Equipment<br>Financing</h3>
  <p>Lorem ipsum dolor sit amet, consectetur adipiscing elit. Ut elit tellus, luctus nec ullamcorper mattis, pulvinar dapibus leo.</p>
</div>
<div class="service-card" style="left:775px">
  <svg width="76" height="76" viewBox="0 0 76 76" fill="none" stroke="#8cc63f" stroke-width="2"><rect x="6" y="12" width="64" height="60"/><path d="M6 24h64M18 6v10M32 6v10M46 6v10M60 6v10M22 60h32v-8H22zM28 52V40h20v12"/></svg>
  <h3>Construction<br>Administrations</h3>
  <p>Lorem ipsum dolor sit amet, consectetur adipiscing elit. Ut elit tellus, luctus nec ullamcorper mattis, pulvinar dapibus leo.</p>
</div>
<div class="btn" style="left:481px;top:1617px;width:237px;height:52px">Our Upcoming Projects</div>

<section>
  <h2 class="section-title" style="left:0;width:1200px;text-align:center;top:1777px;color:var(--blue)">UPCOMING PROJECTS</h2>
  <div class="stripes" style="left:425px;top:1835px;width:350px"></div>
  <div class="project-photo" role="img" aria-label="Photo of a white business park building under a blue sky"></div>
  <h3 class="project-name">Harlow Ridge Business Park</h3>
  <p class="project-sub">Office and light Industrial Building Project</p>
  <p class="project-text">Lorem ipsum dolor sit amet, consectetur adipiscing elit, sed do eiusmod tempor incididunt ut labore et dolore magna aliqua. Ut enim ad minim veniam, quis nostrud exercitation ullamco laboris nisi ut aliquip ex ea commodo consequat. Duis aute irure dolor in reprehenderit in voluptate velit esse cillum dolore eu fugiat nulla pariatu.</p>
  <div class="slide-btn" style="left:655px;top:2237px"><svg width="14" height="18" viewBox="0 0 14 18"><path d="M4 2l7 7-7 7" stroke="#fff" stroke-width="2.5" fill="none"/></svg></div>
  <div class="slide-btn" style="left:600px;top:2290px"><svg width="14" height="18" viewBox="0 0 14 18"><path d="M10 2L3 9l7 7" stroke="#fff" stroke-width="2.5" fill="none"/></svg></div>
</section>

<section class="band" style="top:2390px;height:600px">
  <div class="band-bg" role="img" aria-label="Blue-tinted photo of a professional office building"></div>
  <svg height="600" viewBox="0 0 1200 600">
    <polygon points="0,0 1200,0 1200,40 600,8 0,30" fill="#fff" opacity=".85"/>
  </svg>
</section>
<h2 class="section-title" style="left:0;width:1200px;text-align:center;top:2455px;color:var(--white)">REQUEST A CALL BACK</h2>
<div class="stripes light" style="left:425px;top:2510px;width:350px"></div>
<form class="callback-form">
  <div class="field" style="top:45px">Name</div>
  <div class="field" style="top:96px">Phone</div>
  <div class="field" style="top:146px">Email</div>
  <div class="field" style="top:196px;height:107px">Message</div>
  <div class="send">SEND</div>
</form>

<footer class="site-footer"></footer>
<div class="footer-brand"><span class="brand-dot"></span>VELQ-ORA</div>
<div class="social" style="left:177px;background:#3b5fb0" role="img" aria-label="Social profile"></div>
<div class="social" style="left:212px;background:#2aa3e6" role="img" aria-label="Social profile"></div>
<div class="social" style="left:247px;background:#d8312a" role="img" aria-label="Social profile"></div>
<div class="footer-col">
  <h4 style="left:360px">PARTNERS</h4>
  <a style="left:360px;top:3093px">812 Builders</a>
  <a style="left:360px;top:3121px">Lomerix Equipment Leasing</a>
  <a style="left:360px;top:3148px">Calm Path</a>
  <a style="left:360px;top:3175px">QHZ Dental Services</a>
</div>
<div class="footer-col">
  <h4 style="left:609px">RESOURCES</h4>
  <a style="left:609px;top:3093px">Home</a>
  <a style="left:609px;top:3121px">About Us</a>
  <a style="left:609px;top:3148px">Projects</a>
  <a style="left:609px;top:3175px">Contact Us</a>
</div>
<div class="footer-col">
  <h4 style="left:858px">CONTACTS</h4>
  <svg class="abs" style="left:858px;top:3098px" width="10" height="13" viewBox="0 0 10 13"><path d="M5 0a5 5 0 0 1 5 5c0 3-5 8-5 8S0 8 0 5a5 5 0 0 1 5-5z" fill="#8cc63f"/><circle cx="5" cy="5" r="2" fill="#333"/></svg>
  <span style="left:878px;top:3093px;width:210px">Lorem ipsum dolor sit amet, consectetur adipiscing elit</span>
  <svg class="abs" style="left:857px;top:3153px" width="12" height="12" viewBox="0 0 12 12"><path d="M2 1c.5-.5 1-.5 1.5 0l1.5 2c.3.5 0 1-.4 1.3l-.6.5c.5 1.2 1.4 2 2.5 2.6l.5-.6c.3-.4.9-.6 1.3-.3l2 1.4c.5.4.5 1 0 1.5l-.8.8C8.6 11 7 11 5 9.6 3.3 8.3 2 6.8 1 5 .3 3.6.6 2.4 2 1z" fill="#8cc63f"/></svg>
  <span style="left:878px;top:3148px">812-406-7720</span>
  <svg class="abs" style="left:857px;top:3182px" width="13" height="10" viewBox="0 0 13 10"><rect width="13" height="10" fill="#8cc63f"/><path d="M0 0l6.5 5L13 0" stroke="#333" fill="none"/></svg>
  <span style="left:878px;top:3175px">info@velqorahealth.ca</span>
</div>
<div class="copyright">Copyright © 2020 VELQ-ORA Solutions. All rights reserved.</div>

</body>
</html>
```